Business Card Design

I need a business card design for a new company based in Sydney called 'The Copper Ladle'. We deliver organic, gourmet and fine foods to your door.

I would like to see creative, unique designs which use colours which represent health and nature like green.

Target Market(s)

Health conscious 20 to 35 year olds.

Industry/Entity Type

Health

Contact Information for Business Card

The Copper Ladle, Owen Barclett, owen@thecopperladle.com.au, 0427685392

Requirements
Must have
• My logo.

```html
<!DOCTYPE html>
<html lang="en">
<head>
<meta charset="utf-8">
<title>The Copper Ladle – Business Card</title>
<link rel="stylesheet" href="https://fonts.googleapis.com/css2?family=Open+Sans:wght@300;400;700&display=swap">
<style>
  :root {
    --backdrop: #d9dadc;
    --card: #ffffff;
    --leaf: #8dc21f;
    --leaf-mid: #5aad3a;
    --leaf-deep: #3e8e2f;
    --ink: #4a4a4a;
    --shadow: rgba(0, 0, 0, 0.18);
  }
  * { margin: 0; padding: 0; box-sizing: border-box; }
  html, body {
    width: 1200px;
    height: 800px;
    overflow: hidden;
    background: var(--backdrop);
    font-family: "Open Sans", sans-serif;
    color: var(--ink);
  }
  .stage {
    width: 1200px;
    height: 800px;
    display: flex;
    align-items: center;
    justify-content: center;
    gap: 60px;
  }
  .card {
    position: relative;
    width: 520px;
    height: 297px;
    background: var(--card);
    box-shadow: 0 10px 30px var(--shadow);
    overflow: hidden;
  }

  /* brand lockup */
  .brand {
    display: flex;
    align-items: center;
    gap: 12px;
  }
  .brand-dot {
    width: 40px;
    height: 40px;
    border-radius: 50%;
    background: var(--leaf-mid);
    flex: none;
  }
  .brand-name {
    font-weight: 300;
    font-size: 30px;
    line-height: 1.05;
    color: var(--leaf-deep);
    letter-spacing: 0.5px;
  }

  /* back of card */
  .card-back {
    display: flex;
    flex-direction: column;
    align-items: center;
    justify-content: center;
    gap: 30px;
  }
  .card-back .brand-name { font-size: 32px; }
  .web {
    font-size: 14px;
    color: var(--ink);
  }

  /* front of card */
  .card-front .decor {
    position: absolute;
    left: -130px;
    top: 20px;
    width: 300px;
    height: 300px;
  }
  .card-front .details {
    position: absolute;
    left: 238px;
    top: 52px;
    right: 24px;
  }
  .card-front .brand-name { font-size: 26px; }
  .holder {
    margin-top: 28px;
    font-weight: 700;
    font-size: 15px;
    color: var(--leaf);
  }
  .contact {
    list-style: none;
    margin-top: 12px;
    font-size: 13px;
    line-height: 1.6;
  }
  .contact li {
    display: flex;
    align-items: center;
    gap: 8px;
  }
  .contact svg {
    width: 11px;
    height: 11px;
    flex: none;
  }
  .contact .web { font-size: 13px; }
</style>
</head>
<body>
<main class="stage">

  <section class="card card-back" aria-label="Business card, back">
    <div class="brand">
      <span class="brand-dot"></span>
      <span class="brand-name">The Copper Ladle</span>
    </div>
    <p class="web">www.thecopperladle.com.au</p>
  </section>

  <section class="card card-front" aria-label="Business card, front">
    <svg class="decor" viewBox="0 0 300 300" role="img" aria-label="Large green brand decoration">
      <defs>
        <linearGradient id="decorFill" x1="0" y1="0" x2="1" y2="1">
          <stop offset="0" stop-color="#5aad3a"/>
          <stop offset="1" stop-color="#9cc41f"/>
        </linearGradient>
      </defs>
      <circle cx="150" cy="150" r="150" fill="url(#decorFill)"/>
    </svg>

    <div class="details">
      <div class="brand">
        <span class="brand-dot"></span>
        <span class="brand-name">The Copper Ladle</span>
      </div>
      <p class="holder">Owen Barclett</p>
      <ul class="contact">
        <li>
          <svg viewBox="0 0 12 12" aria-hidden="true"><rect x="3" y="0.5" width="6" height="11" rx="1.2" fill="none" stroke="var(--leaf)" stroke-width="1.3"/><circle cx="6" cy="9.3" r="0.8" fill="var(--leaf)"/></svg>
          <span>0427685392</span>
        </li>
        <li>
          <svg viewBox="0 0 12 12" aria-hidden="true"><rect x="0.7" y="2.2" width="10.6" height="7.6" fill="none" stroke="var(--leaf)" stroke-width="1.3"/><path d="M1 2.6 L6 6.6 L11 2.6" fill="none" stroke="var(--leaf)" stroke-width="1.3"/></svg>
          <span>owen@thecopperladle.com.au</span>
        </li>
        <li><span class="web">www.thecopperladle.com.au</span></li>
      </ul>
    </div>
  </section>

</main>
</body>
</html>
```